Creative Businesss Card desgin!

Create a business card for our business Glint window cleaning!
We are open to creative ideas as long as it maintains a professional image.

Target Market(s)

Small Commercial window cleaning clients including car dealerships, strata manager, cafe

Industry/Entity Type

Window Cleaning

Contact Information for Business Card

Darren Pilkey
General Manager
Glint Window Cleaning

darren@glintservices.com.au
pane-tidy-corner.com.au
Ph: 1800 GO GLINT
Mob: 0438 572 619

Colors
fbed22
0392cd

Requirements
Should not have
• Stock window cleaning/ squeegee graphics

```html
<!DOCTYPE html>
<html lang="en">
<head>
<meta charset="UTF-8">
<title>Glint Window Cleaning – Business Card</title>
<link rel="stylesheet" href="https://fonts.googleapis.com/css2?family=Lato:wght@300;400;700;900&display=swap">
<style>
  :root {
    --brand-blue: #0d5c95;
    --pill-blue: #1d8fd8;
    --brand-yellow: #fbed22;
    --paper: #ffffff;
    --stage: #2c3038;
    --card-w: 340px;
    --card-h: 556px;
    --radius: 28px;
  }
  * { box-sizing: border-box; margin: 0; padding: 0; }
  html, body {
    width: 1200px; height: 900px; overflow: hidden;
    background: var(--stage);
    font-family: "Lato", sans-serif;
  }
  .card {
    position: absolute;
    top: 172px;
    width: var(--card-w); height: var(--card-h);
    border-radius: var(--radius);
    overflow: hidden;
    background: var(--paper);
    box-shadow: 0 14px 30px rgba(0,0,0,.35);
  }
  .card--front { left: 220px; }
  .card--back { left: 640px; }
  .card__shape { position: absolute; inset: 0; width: 100%; height: 100%; }
  .wordmark {
    position: absolute; left: 0; right: 0;
    text-align: center;
    color: var(--brand-yellow);
    font-weight: 900;
    line-height: 1;
  }
  .wordmark__name { display: block; font-size: 40px; letter-spacing: 2px; }
  .wordmark__tag { display: block; font-size: 10.5px; letter-spacing: 1.4px; margin-top: 4px; }
  .card--front .wordmark { top: 108px; }
  .card--back .wordmark { top: 128px; }

  .person { position: absolute; left: 30px; top: 226px; color: var(--paper); }
  .person__name { font-size: 26px; line-height: 1; letter-spacing: .3px; }
  .person__first { font-weight: 900; }
  .person__last { font-weight: 300; color: var(--brand-yellow); }
  .person__role { font-size: 13px; font-weight: 300; letter-spacing: .5px; margin-top: 3px; }

  .contacts { position: absolute; left: 30px; top: 282px; list-style: none; }
  .contacts__row { display: flex; align-items: center; height: 24px; color: var(--paper); font-size: 14px; }
  .contacts__label {
    width: 40px; margin-right: 10px;
    background: var(--pill-blue); border-radius: 9px;
    font-size: 11px; text-align: center; line-height: 17px;
  }
  .site-url {
    position: absolute; left: 0; right: 0; top: 482px;
    text-align: center; color: var(--paper); font-size: 14px; letter-spacing: .3px;
  }
</style>
</head>
<body>
  <section class="card card--front" aria-label="Business card front">
    <svg class="card__shape" viewBox="0 0 340 556" aria-hidden="true">
      <path fill="var(--brand-blue)" d="M0 0 H340 V392 H212 C186 392 190 446 164 446 H0 Z"/>
    </svg>
    <div class="wordmark">
      <span class="wordmark__name">GLINT</span>
      <span class="wordmark__tag">WINDOW CLEANING</span>
    </div>
    <div class="person">
      <p class="person__name"><span class="person__first">DARREN</span> <span class="person__last">PILKEY</span></p>
      <p class="person__role">GENERAL MANAGER</p>
    </div>
    <ul class="contacts">
      <li class="contacts__row"><span class="contacts__label">Mob</span>0438 572 619</li>
      <li class="contacts__row"><span class="contacts__label">Ph</span>1800 GO GLINT</li>
      <li class="contacts__row"><span class="contacts__label">Mail</span>darren@glintservices.com.au</li>
      <li class="contacts__row"><span class="contacts__label">Web</span>pane-tidy-corner.com.au</li>
    </ul>
  </section>

  <section class="card card--back" aria-label="Business card back">
    <svg class="card__shape" viewBox="0 0 340 556" aria-hidden="true">
      <path fill="var(--brand-blue)" d="M0 514 H30 C54 514 50 466 76 466 H262 C288 466 286 508 310 508 H340 V556 H0 Z"/>
    </svg>
    <div class="wordmark">
      <span class="wordmark__name">GLINT</span>
      <span class="wordmark__tag">WINDOW CLEANING</span>
    </div>
    <p class="site-url">pane-tidy-corner.com.au</p>
  </section>
</body>
</html>
```